2-Sided A4 Brochure

We're looking for a double-sided A4 brochure for print and PDF. Company is in online travel and is called "Pebble Lantern". This brochure is intended for partner organisations looking to license our technology for use on their websites. As such, the design should maintain the inspirational feel of typical travel designs whilst also conveying a good deal of professionalism.
A selection of images we've taken from the technology has be supplied along with logo and copy. Please utilise at least a few of these images in any and all designs.
Preferred colours are #56A0CD and #00286B. Copy includes headings and contact details should be in a breakout box.
Finished size: 210mm x 297mm
Bleed size (2mm): 214mm x 301mm
Safe size (5mm): 204mm x 291mm
Industry/Entity Type
Travel
Look and feel
Each slider illustrates characteristics of the customer's brand and the style your logo design should communicate.

```html
<!DOCTYPE html>
<html lang="en">
<head>
<meta charset="utf-8">
<title>Pebble Lantern – Partner Brochure</title>
<link rel="stylesheet" href="https://fonts.googleapis.com/css2?family=Anton&family=Nunito+Sans:wght@300;400&family=Nunito:wght@600&display=swap">
<style>
  :root{
    --sky:#56A0CD;
    --navy:#00286B;
    --royal:#27418f;
    --heading:#3f97cf;
    --body:#3a3a3a;
    --link:#5aa7d6;
    --page:#ffffff;
    --backdrop:#e8e6e2;
    --body-font:"Nunito Sans", Arial, sans-serif;
  }
  *{box-sizing:border-box;margin:0;padding:0}
  html,body{width:1200px;height:907px;overflow:hidden;background:var(--backdrop)}
  .sheet{
    position:absolute;left:61px;top:73px;width:1078px;height:765px;
    background:var(--page);overflow:hidden;
    box-shadow:0 4px 14px rgba(0,0,0,.18);
    font-family:var(--body-font);color:var(--body);
  }
  .header-band{position:absolute;left:0;top:0;width:1078px;height:121px}
  .brand{position:absolute;left:19px;top:28px}
  .brand-name{font-family:"Nunito",sans-serif;font-weight:600;font-size:29px;color:#1f7fb4;letter-spacing:-.3px;line-height:1}
  .brand-tagline{position:absolute;left:154px;top:38px;white-space:nowrap;font-size:9px;color:var(--navy);font-weight:400}
  .headline{position:absolute;left:744px;top:8px;width:320px;height:330px}
  .column{position:absolute;font-size:12px;line-height:13.7px;font-weight:300;text-align:justify;hyphens:auto}
  .column h2{font-weight:400;font-size:15px;line-height:17px;color:var(--heading);text-align:left}
  .col-left{left:33px;top:144px;width:334px}
  .col-middle{left:388px;top:140px;width:334px}
  .col-right{left:747px;top:367px;width:300px}
  .photo{position:absolute}
  .photo-bridge{left:33px;top:322px;width:335px;height:212px;
    background:linear-gradient(180deg,#3d8fd8 0%,#79b6e8 55%,#9fb7c4 70%,#2f4a60 100%)}
  .section-lower{position:absolute;left:33px;top:558px;width:334px}
  .gap{height:22px}
  .float-spacer{float:right;width:0;height:270px}
  .phone-reserve{float:right;clear:right;width:176px;height:326px}
  .phone{position:absolute;left:566px;top:410px;width:155px;height:314px;border-radius:24px;
    background:linear-gradient(180deg,#1b1b1b 0%,#3a3a3a 50%,#151515 100%);z-index:2}
  .contact{position:absolute;right:40px;top:568px;text-align:right;font-weight:300}
  .contact h3{font-weight:400;font-size:19px;color:var(--royal);line-height:24px}
  .contact p{font-size:15px;line-height:21px;color:var(--link)}
  .beach{position:absolute;left:0;top:660px;width:1078px;height:105px;border-top:2px solid var(--navy);
    background:linear-gradient(180deg,#8fc9ec 0%,#c9e6f4 30%,#3fc6d0 48%,#6fdbd8 68%,#e9e4cf 100%)}
</style>
</head>
<body>
<main class="sheet">
  <svg class="header-band" viewBox="0 0 1078 121" aria-hidden="true">
    <defs>
      <linearGradient id="bandGrad" x1="0" y1="0" x2="1" y2="0">
        <stop offset="0" stop-color="#56A0CD"/>
        <stop offset=".45" stop-color="#3f78b6"/>
        <stop offset="1" stop-color="#27418f"/>
      </linearGradient>
    </defs>
    <rect width="1078" height="121" fill="url(#bandGrad)"/>
    <rect x="0" y="91" width="820" height="30" fill="#56A0CD" opacity=".55"/>
    <polygon points="0,0 385,0 300,96 0,96" fill="#00286B"/>
    <polygon points="0,0 373,0 291,88 0,88" fill="#ffffff"/>
  </svg>

  <div class="brand">
    <div class="brand-name">Pebble Lantern</div>
    <div class="brand-tagline">Where great journeys begin.</div>
  </div>

  <svg class="headline" viewBox="0 0 320 330" role="img" aria-label="Where great journeys begin">
    <defs>
      <linearGradient id="skyFill" x1="0" y1="0" x2="0" y2="1">
        <stop offset="0" stop-color="#e8f6ff"/><stop offset="1" stop-color="#7ec8f0"/>
      </linearGradient>
      <linearGradient id="seaFill" x1="0" y1="0" x2="0" y2="1">
        <stop offset="0" stop-color="#2aa7c9"/><stop offset="1" stop-color="#7fd6dd"/>
      </linearGradient>
      <linearGradient id="surfFill" x1="0" y1="0" x2="0" y2="1">
        <stop offset="0" stop-color="#f4f1ea"/><stop offset="1" stop-color="#b8b1a4"/>
      </linearGradient>
      <linearGradient id="sandFill" x1="0" y1="0" x2="0" y2="1">
        <stop offset="0" stop-color="#ead6b8"/><stop offset="1" stop-color="#b98f66"/>
      </linearGradient>
    </defs>
    <g font-family="Anton, sans-serif" font-size="86">
      <text x="2" y="80" textLength="216" lengthAdjust="spacingAndGlyphs" fill="url(#skyFill)">WHERE</text>
      <text x="2" y="162" textLength="196" lengthAdjust="spacingAndGlyphs" fill="url(#seaFill)">GREAT</text>
      <text x="0" y="244" textLength="300" lengthAdjust="spacingAndGlyphs" fill="url(#surfFill)">JOURNEYS</text>
      <text x="2" y="326" textLength="182" lengthAdjust="spacingAndGlyphs" fill="url(#sandFill)">BEGIN</text>
    </g>
  </svg>

  <section class="column col-left">
    <h2>Pebble Lantern for Tourism Organizations</h2>
    <p>Pebble Lantern offers travelers the most powerful and convenient way to plan and book their next fantastic getaway. Selecting from flights, hotels, tours, cruises, restaurants, activities and more, travelers can create custom itineraries complete with a personalized, full-color brochure before sharing them with friends or submitting them anonymously for quotes from hundreds of travel agents. Pebble Lantern’s industry-leading, patent-pending technology mirrors the experience of visiting the local, high-street travel agency whilst affording the privacy, convenience and power of transacting online.</p>
  </section>

  <div class="photo photo-bridge" role="img" aria-label="Photo of a suspension bridge over a river beneath a blue sky"></div>

  <section class="column section-lower">
    <h2>Not Just a Planner – Not Just a Booking Engine</h2>
    <p>Travel planners simply plan while booking engines simply book – Pebble Lantern bridges this gap by combining the convenience of the internet with the trust and protection of registered travel agents. With no affiliation to content providers, Pebble</p>
  </section>

  <section class="column col-middle">
    <div class="float-spacer"></div>
    <div class="phone-reserve"></div>
    <p>Lantern is free to promote the content best suited to your users. And when the user has compiled their ideal itinerary from our vast range of tailored product, they can send their itinerary to hundreds of travel agents for a free, anonymous quote.</p>
    <p>Pebble Lantern charges no membership fees to users meaning our service is offered completely free of charge to travelers. Instead, travel agents subscribe to receive and quote on the itineraries submitted via the site. This means that our goal and your goal are the same: getting people to your destination.</p>
    <div class="gap"></div>
    <h2>Our Technology, Your Brand</h2>
    <p>We are passionate about our reputation as trusted and unbiased providers of travel advice. Our brand is important to us; just as yours is to you.</p>
    <p>Many holiday planners are light on features offering only basic search functionality on your site before clicking through to theirs. With just a few lines of HTML, Pebble Lantern is completely integrated into your site allowing users to build an entire itinerary never leaving your page. Without ever clicking-through, clicking-out or popping-up, users can search for content, view high-resolution images, consult detailed maps, create their itinerary and print or share their customized brochure with friends. This means you can leverage the industry-leading technology of Pebble Lantern all the while protecting your brand asset.</p>
  </section>

  <div class="phone" role="img" aria-label="Smartphone showing the itinerary planner with destination photos and listings"></div>

  <section class="column col-right">
    <h2>Travel is Social</h2>
    <p>Travelers love to share their experiences and what better way than by the power of social media. Pebble Lantern not only offers complete web integration with leading social media such as Chatterbook, Tweetline and Circlespace but is also available as a fully-branded Chatterbook app and mobile app. You can offer your users the power and convenience of Pebble Lantern via the channel of their choice with all interactions linked back directly to your social media presence. Leverage the virality and interactivity of social media with Pebble Lantern’s seamless integration into your own social media assets.</p>
  </section>

  <aside class="contact">
    <h3>Contact Details</h3>
    <p>www.pebblelantern.com</p>
    <p>partners@pebblelantern.com</p>
  </aside>

  <div class="beach" role="img" aria-label="Panoramic photo of a tropical beach with turquoise water, boats and palm-covered islands"></div>
</main>
</body>
</html>
```